11 x 17 Orvanthes Quote

Design the following quote in a poster.

"First say to yourself what you would be; then do what you have to do." - Orvanthes

See here for inspiration - https://prints.mornbrekal.com/

Quote

```html
<!DOCTYPE html>
<html lang="en">
<head>
<meta charset="utf-8">
<title>Orvanthes Quote Poster</title>
<link rel="stylesheet" href="https://fonts.googleapis.com/css2?family=Bebas+Neue&display=swap">
<style>
  :root {
    --poster-red: #e3171b;
    --poster-red-deep: #b80f13;
    --portrait-shade: #a50d12;
    --quote-white: #f4f1f1;
    --quote-grey: #d9d4d4;
    --accent-yellow: #f2d21a;
  }
  html, body {
    margin: 0;
    padding: 0;
    width: 777px;
    height: 1200px;
    overflow: hidden;
    background: var(--poster-red);
  }
  .poster {
    position: relative;
    width: 777px;
    height: 1200px;
    background:
      radial-gradient(ellipse at 50% 45%, var(--poster-red) 0%, var(--poster-red) 55%, var(--poster-red-deep) 100%);
    overflow: hidden;
  }
  .portrait-area {
    position: absolute;
    left: 90px;
    top: 330px;
    width: 640px;
    height: 870px;
    border-radius: 48% 52% 0 0 / 38% 38% 0 0;
    background: radial-gradient(ellipse at 50% 35%, var(--portrait-shade) 0%, rgba(165, 13, 18, 0.55) 45%, rgba(165, 13, 18, 0) 75%);
  }
  .quote-layout {
    position: absolute;
    inset: 0;
    width: 777px;
    height: 1200px;
  }
  .quote-line {
    font-family: "Bebas Neue", "Arial Narrow", sans-serif;
    fill: url(#quote-fill);
  }
  .author-name {
    font-family: "Bebas Neue", "Arial Narrow", sans-serif;
    fill: var(--quote-white);
  }
  .attribution-rule {
    fill: none;
    stroke: var(--accent-yellow);
    stroke-width: 5;
    stroke-linejoin: miter;
  }
</style>
</head>
<body>
<main class="poster">
  <div class="portrait-area" role="img" aria-label="Faded red-toned photograph of a woman in profile behind the quote"></div>

  <svg class="quote-layout" viewBox="0 0 777 1200" xmlns="http://www.w3.org/2000/svg">
    <defs>
      <linearGradient id="quote-fill" x1="0" y1="0" x2="0" y2="1">
        <stop offset="0" stop-color="var(--quote-white)"/>
        <stop offset="1" stop-color="var(--quote-grey)"/>
      </linearGradient>
    </defs>

    <text class="quote-line" x="389" y="163" font-size="62" text-anchor="middle" textLength="329" lengthAdjust="spacingAndGlyphs">FIRST SAY TO</text>
    <text class="quote-line" x="389" y="343" font-size="172" text-anchor="middle" textLength="511" lengthAdjust="spacingAndGlyphs">YOURSELF</text>
    <text class="quote-line" x="402" y="489" font-size="90" text-anchor="middle" textLength="472" lengthAdjust="spacingAndGlyphs">WHAT YOU WOULD</text>
    <text class="quote-line" x="388" y="652" font-size="148" text-anchor="middle" textLength="124" lengthAdjust="spacingAndGlyphs">BE;</text>
    <text class="quote-line" x="391" y="780" font-size="76" text-anchor="middle" textLength="494" lengthAdjust="spacingAndGlyphs">THEN DO WHAT YOU</text>
    <text class="quote-line" x="388" y="892" font-size="80" text-anchor="middle" textLength="276" lengthAdjust="spacingAndGlyphs">HAVE TO DO</text>

    <path class="attribution-rule" d="M269 955 H338 L352 973 L352 955 H525"/>

    <text class="author-name" x="389" y="1029" font-size="50" text-anchor="middle" textLength="210" lengthAdjust="spacingAndGlyphs">ORVANTHES</text>
  </svg>
</main>
</body>
</html>
```